VoltNest EV Charger Installation

We are an electrical contractor "Brannock Electric" http://brannockelectricworks.example.

New site is for a division we are creating. http://voltnestelectric.example/ is registered on Google domains.
Company is registered as VoltNest LLC.
VoltNest is something we are trying out to see if we can find a niche installing EV chargers and EV Charger outlets in existing homes and businesses. Looking to work it as a division off from Brannock Electric short term and if successful it would become a stand alone business. Often times this requires additional work to meet code. Work such as adding smoke & carbon monoxide detectors, new electrical panels and upgrading the electrical Main Service Meter system.
Will need to coordinate this site with our current Brannock Electric website. Not sure how this can work. We like the look of our current Brannock Electric Wordpress site, but it is dated and broken, in need of a rebuild or repair as well.
Need a website as a landing point for Google Maps inquiries and possibly as a way to drive customers to call for our services. Need to be mindful that we want to avoid confusion with people looking for EV charger Stations to drive and plug in their cars. We are a contractor not a place to plug in! The name may be problematic in this sense.
Looking for a site that coordinates style & color with the provided VoltNest logo. Would like to have a contact / inquiry page with a captcha or similar tool to weed out spam. need to integrate google maps and similar tools to measure marketing, assist in lead generation, etc.
Have Logo artwork. Not sure what format is best to upload.

Target Market(s)

People with electric cars, business owners and homeowners.

Industry/Entity Type

Electrical Contractor- Residential & Light Commercial (mostly residential)

Requirements
Must have
• Landing Page/about us , Contact Us/ inquiry Page with a quality captcha filter, Job Gallery- we don't have many pics yet. Google pointers /tools. Open to suggestions here! Mobile Phone/ Tablet friendly is important. I listed coded design but not quite sure what that means.
Nice to have
• Similar to the Brannock Electric site style a possibility, but open to suggestions. Possibly have something that shows the business is connected to Brannock Electric? ..."A division of Brannock Electric" with logo/link to site?

```html
<!DOCTYPE html>
<html lang="en">
<head>
<meta charset="utf-8">
<title>VoltNest EV Charger Installation</title>
<link rel="stylesheet" href="https://fonts.googleapis.com/css2?family=Orbitron:wght@800;900&family=Poppins:wght@400;500&display=swap">
<style>
:root{
  --green:#8cc63f;
  --green-band:#93c653;
  --green-deep:#7fb536;
  --ink:#111111;
  --text:#444444;
  --white:#ffffff;
  --black:#000000;
  --line:#cfcfcf;
}
*{margin:0;padding:0;box-sizing:border-box}
html,body{width:1200px;height:3227px;overflow:hidden;background:var(--white)}
body{position:relative;font-family:"Poppins",sans-serif;color:var(--text)}
.abs{position:absolute}
.display{font-family:"Orbitron",sans-serif;font-weight:900;text-transform:uppercase;letter-spacing:1px;color:var(--ink);line-height:41px;font-size:31px;white-space:nowrap}
.display .hl{color:var(--green)}
.body-text{font-size:13.5px;line-height:21px;color:var(--text)}
.btn{position:absolute;display:flex;align-items:center;justify-content:center;border-radius:20px;font-size:13px;font-weight:500;white-space:nowrap}
.btn-green{background:var(--green);color:var(--white)}
.photo{position:absolute}
.hero{position:absolute;left:0;top:0;width:1200px;height:675px;background:linear-gradient(90deg,#3a3a3a 0%,#2f2f2f 45%,#4a4a4a 70%,#2b2b2b 100%)}
.topbar{position:absolute;left:0;top:0;width:1200px;height:32px;color:var(--white);font-size:12px}
.nav{position:absolute;left:60px;top:34px;width:1080px;height:67px;background:var(--white);border-radius:4px}
.logo{position:absolute;display:flex;align-items:center;gap:8px;font-family:"Orbitron",sans-serif;font-weight:900;color:var(--ink);white-space:nowrap}
.logo .dot{width:22px;height:22px;border-radius:50%;background:var(--green)}
.nav-links{position:absolute;left:442px;top:24px;display:flex;gap:38px;font-size:13.5px;font-weight:500;color:var(--ink);white-space:nowrap}
.nav-links .active{color:var(--green)}
.call{position:absolute;left:871px;top:14px;width:192px;height:39px;background:var(--green);border-radius:5px;color:var(--white);display:flex;align-items:center;white-space:nowrap}
.call small{font-size:9px;line-height:11px;text-align:center;width:56px;flex:none;border-right:1px solid rgba(255,255,255,.6)}
.call b{font-family:"Orbitron",sans-serif;font-weight:800;font-size:12px;margin-left:10px;letter-spacing:0;white-space:nowrap}
.hero-head{font-size:44px;line-height:57px;color:var(--white)}
.foot-h{font-family:"Orbitron",sans-serif;font-weight:800;font-size:13px;color:var(--green);text-transform:uppercase;letter-spacing:1px;line-height:22px}
.foot-links{font-size:12.5px;color:var(--ink);line-height:30px}
.social{position:absolute;width:36px;height:36px;border-radius:50%;border:1px solid #333}
.social.fill{background:var(--green);border-color:var(--green)}
</style>
</head>
<body>

<section class="hero" role="img" aria-label="Dark garage with an electric car plugged into a wall-mounted charger"></section>
<div class="topbar">
  <svg class="abs" style="left:60px;top:10px" width="16" height="12" viewBox="0 0 16 12"><rect width="16" height="12" rx="1" fill="#8cc63f"/><path d="M1 1l7 6 7-6" stroke="#2a2a2a" stroke-width="1.5" fill="none"/></svg>
  <span class="abs" style="left:84px;top:8px">E-mail Us: info@voltnest.example</span>
  <span class="abs" style="left:1007px;top:8px">Follow Us:</span>
  <span class="abs" style="left:1076px;top:11px;width:10px;height:10px;border-radius:50%;background:var(--green)"></span>
  <span class="abs" style="left:1102px;top:11px;width:10px;height:10px;border-radius:50%;background:var(--white)"></span>
  <span class="abs" style="left:1126px;top:11px;width:10px;height:10px;border-radius:50%;background:var(--white)"></span>
</div>
<header class="nav">
  <div class="logo" style="left:26px;top:18px;font-size:26px"><span class="dot"></span>VoltNest</div>
  <nav class="nav-links"><span class="active">Home</span><span>Charging Solution</span><span>About Us</span><span>Contact us</span></nav>
  <div class="call"><small>Call Us<br>Today</small><b>555-014-2290</b></div>
</header>
<p class="abs" style="left:61px;top:222px;font-size:16px;color:var(--white);font-weight:500">Need an electric car charger?</p>
<h1 class="abs display hero-head" style="left:61px;top:250px"><span class="hl">Let VoltNest</span><br>help you get<br>powered up!</h1>
<p class="abs" style="left:61px;top:426px;font-size:14px;color:var(--white)">Electric vehicles (EVs) are here. Let VoltNest help you get powered up!</p>
<div class="btn" style="left:60px;top:477px;width:162px;height:36px;border:2px solid var(--green);color:var(--white)">Get A Free Quote</div>
<span class="abs" style="left:580px;top:605px;width:8px;height:8px;border-radius:50%;background:var(--white)"></span>
<span class="abs" style="left:593px;top:601px;width:14px;height:14px;border-radius:50%;border:2px solid var(--green)"></span>
<span class="abs" style="left:597px;top:605px;width:6px;height:6px;border-radius:50%;background:var(--green)"></span>
<span class="abs" style="left:612px;top:605px;width:8px;height:8px;border-radius:50%;background:var(--white)"></span>
<span class="abs" style="left:599px;top:615px;width:2px;height:60px;background:var(--green)"></span>

<div class="photo" style="left:60px;top:750px;width:262px;height:337px;background:linear-gradient(160deg,#d9d3c3,#a9a59c 60%,#6e6a64)" role="img" aria-label="Wall charger installed beside a parked silver SUV in a garage"></div>
<div class="photo" style="left:336px;top:804px;width:263px;height:337px;background:linear-gradient(180deg,#e9e7e2,#cfcac0)" role="img" aria-label="Open residential electrical panel with breakers"></div>
<h2 class="abs display" style="left:638px;top:782px">We provide best<br>solutions for <span class="hl">your</span><br><span class="hl">electric vehicle</span></h2>
<p class="abs body-text" style="left:637px;top:910px;width:495px">EV charger installation is a relatively simple process, but it's important to hire a qualified electrician. VoltNest is a division of Brannock Electric, a licensed and insured electrical contractor. We are committed to providing our customers with a quality, code approved installation.</p>
<p class="abs body-text" style="left:637px;top:1000px;width:495px">The cost of EV charger installation will vary depending on a number of factors, including the type of charger, the distance and access to the electrical panel. Typical charger installations range from $600 to $2,000</p>
<div class="btn btn-green" style="left:636px;top:1087px;width:161px;height:37px">Get A Free Quote</div>

<h2 class="abs display" style="left:61px;top:1283px">Once your <span class="hl">EV</span><br><span class="hl">charger is</span><br><span class="hl">installed</span></h2>
<p class="abs body-text" style="left:61px;top:1412px;width:345px">Once your EV charger is installed, you'll start enjoying the convenience of at home/business charging and the many benefits of owning an EV.</p>
<div class="photo" style="left:520px;top:1216px;width:450px;height:390px;background:linear-gradient(180deg,#b8a98e,#c9b99a 60%,#9c8a70)" role="img" aria-label="Basement wall with battery storage unit and electrical panels"></div>
<div class="photo" style="left:977px;top:1216px;width:163px;height:126px;background:linear-gradient(90deg,#7a6a4c,#a07a52)" role="img" aria-label="Exterior meter on wooden framing"></div>
<div class="photo" style="left:977px;top:1348px;width:163px;height:126px;background:linear-gradient(180deg,#e6dfd0,#cfc6b4)" role="img" aria-label="Wall mounted EV charger"></div>
<div class="photo" style="left:977px;top:1481px;width:163px;height:125px;background:linear-gradient(180deg,#dedad2,#c4c0b8)" role="img" aria-label="EV charger with cable on garage wall"></div>

<section class="abs" style="left:0;top:1685px;width:1200px;height:322px;background:var(--green-band)"></section>
<div class="photo" style="left:523px;top:1726px;width:128px;height:230px;border-radius:14px;background:var(--green-deep);opacity:.55" role="img" aria-label="Faint wall charger unit in the background"></div>
<h2 class="abs display" style="left:0;top:1766px;width:1200px;text-align:center;color:var(--white)">Ready to take action?</h2>
<p class="abs" style="left:330px;top:1814px;width:540px;text-align:center;font-size:13.5px;line-height:21px;color:var(--white)">We look forward to discussing your EV charger installation evaluation and estimate.</p>
<div class="btn" style="left:491px;top:1880px;width:218px;height:37px;background:var(--white);color:var(--ink)">Contact VoltNest Today</div>

<div class="photo" style="left:60px;top:2083px;width:495px;height:411px;background:linear-gradient(120deg,#8c8c88,#5e5d58 50%,#a89a7c)" role="img" aria-label="Electrician in a hard hat working on an electrical panel"></div>
<h2 class="abs display" style="left:619px;top:2126px">VoltNest will<br>acquire the required<br><span class="hl">electrical permit</span><br><span class="hl">for your job</span></h2>
<p class="abs body-text" style="left:618px;top:2296px;width:522px">Lorem Ipsum is simply dummy text of the printing and typesetting industry. Lorem Ipsum has been the industry's standard dummy text ever since the 1500s, when an unknown printer took a galley of type and scrambled it to make a type specimen book.</p>
<div class="btn btn-green" style="left:618px;top:2405px;width:160px;height:36px">Get A Free Quote</div>

<section class="abs" style="left:0;top:2578px;width:1200px;height:338px;background:var(--black)"></section>
<div class="photo" style="left:782px;top:2528px;width:236px;height:388px;border-radius:30px 30px 0 0;border:6px solid #222;background:linear-gradient(160deg,#e8e8e8,#cfcfcf)" role="img" aria-label="Smartphone showing a map with a location pin"></div>
<h2 class="abs display" style="left:61px;top:2624px;color:var(--white)">Help find a safe and<br>convenient <span class="hl">location</span><br><span class="hl">for the charger.</span></h2>
<p class="abs" style="left:61px;top:2753px;width:520px;font-size:13.5px;line-height:21px;color:var(--white)">We can help you determine if any upgrades are necessary and can provide you with a quote for the work.</p>
<div class="btn btn-green" style="left:60px;top:2813px;width:162px;height:37px">Get A Free Quote</div>

<footer>
  <div class="logo" style="left:60px;top:3000px;font-size:27px"><span class="dot"></span>VoltNest</div>
  <span class="social" style="left:60px;top:3058px"></span>
  <span class="social fill" style="left:106px;top:3058px"></span>
  <span class="social" style="left:152px;top:3058px"></span>

  <h3 class="abs foot-h" style="left:337px;top:2980px">Quick links</h3>
  <span class="abs" style="left:337px;top:3006px;width:90px;height:2px;background:var(--green)"></span>
  <div class="abs foot-links" style="left:337px;top:3018px">Home<br>Charging Solution<br>About Us<br>Contact us</div>

  <h3 class="abs foot-h" style="left:613px;top:2980px">Contact us</h3>
  <span class="abs" style="left:613px;top:3006px;width:90px;height:2px;background:var(--green)"></span>
  <svg class="abs" style="left:612px;top:3026px" width="14" height="18" viewBox="0 0 14 18"><path d="M7 0a7 7 0 0 0-7 7c0 5 7 11 7 11s7-6 7-11a7 7 0 0 0-7-7z" fill="#8cc63f"/><circle cx="7" cy="7" r="2.6" fill="#fff"/></svg>
  <p class="abs" style="left:641px;top:3020px;width:215px;font-size:12.5px;line-height:20px;color:var(--ink)">123, Lorem Ipsum Is A dummy text of the printing</p>
  <svg class="abs" style="left:612px;top:3074px" width="14" height="14" viewBox="0 0 24 24"><path d="M6.6 10.8a15 15 0 0 0 6.6 6.6l2.2-2.2a1 1 0 0 1 1-.25 11.4 11.4 0 0 0 3.6.6 1 1 0 0 1 1 1V20a1 1 0 0 1-1 1A17 17 0 0 1 3 4a1 1 0 0 1 1-1h3.5a1 1 0 0 1 1 1c0 1.25.2 2.45.6 3.6a1 1 0 0 1-.25 1z" fill="#8cc63f"/></svg>
  <p class="abs" style="left:641px;top:3071px;font-size:12.5px;color:var(--ink);font-weight:500">555 014 2290</p>
  <svg class="abs" style="left:612px;top:3108px" width="16" height="12" viewBox="0 0 16 12"><rect width="16" height="12" rx="1" fill="#8cc63f"/><path d="M1 1l7 6 7-6" stroke="#fff" stroke-width="1.5" fill="none"/></svg>
  <p class="abs" style="left:641px;top:3104px;font-size:12.5px;color:var(--ink)">info@voltnest.example</p>

  <h3 class="abs foot-h" style="left:889px;top:2980px">Subscribe to our<br>newslatter</h3>
  <div class="abs" style="left:888px;top:3038px;width:253px;height:35px;border:1px solid #333;border-radius:18px;font-size:12px;color:var(--ink);padding:9px 20px">E-mail*</div>
  <div class="btn btn-green" style="left:888px;top:3084px;width:253px;height:32px;font-weight:400">Subscribe</div>

  <span class="abs" style="left:0;top:3189px;width:1200px;height:1px;background:var(--line)"></span>
  <p class="abs" style="left:0;top:3199px;width:1200px;text-align:center;font-size:12px;color:var(--ink)">© Copyright 2023 VoltNest. All Rights Reserved.</p>
</footer>

</body>
</html>
```